Mobile App UI for Telecommunications/Hosting Company

We are about to convert our existing self-service Customer Portal into a mobile phone application and need an elegant and professional UI/UX design. Our company provides telecommunication (voice/mobile/data) and hosting services to medium-sized business. The primary purpose of the application is to view trouble tickets, alerts, orders, and performance charts. This application is available to customers only - not the general public.

Please provide a UI design suitable for display on iPhone/Android devices. The attached document includes a proposed screen flow. You are free to design your own screens to display the same information elegantly.
Updates

Please note that the design should be based on the wireframes in the Word document, not the screenshots.  The screenshots are just to show our existing web portal look & feel.

Also, just a few screens are required for initial submission (3 would be great).

Thanks,
Dermot.

Target Market(s)

IT Managers away from their desk and using a mobile phone application.
Adult males from technical background aged 30-50.
Customers of Brindlewood Networks have access to this application (not the general public). This is a self-service portal for customers only.

Industry/Entity Type

Business

Colors
0592cd
33a6d7
85cae6
cadf82
fde08a

Requirements
Must have
• Please look at the screenshots from our current Customer Portal site (part of the project brief). The mobile app does not have to look the same, but should follow a similar style.

Please check out our company web site at www.brindlewoodnetworks.example (this site is not the customer portal and has a different look at feel) to understand what Brindlewood Networks does.
Nice to have
• Sharing capabilities via email/SMS.
A nice background image to make it stand out
The colours selected below are a guide only as they are similar to the corporate colours
- The priority is something that works on a phone - a design extendable to tablets is a nice to have as our existing web site looks OK on a tablet..

```html
<!DOCTYPE html>
<html lang="en">
<head>
<meta charset="utf-8">
<title>Brindlewood Networks – Login</title>
<link rel="stylesheet" href="https://fonts.googleapis.com/css2?family=Noto+Sans:ital,wght@0,400;1,400&display=swap">
<style>
  :root {
    --page-bg: #eef3f6;
    --frame: #dce1e5;
    --panel-dark: #2b2b2b;
    --panel-dark-hi: #3a3a3a;
    --accent: #3bc4ea;
    --accent-deep: #33b6dd;
    --brand-text: #2b2b2b;
    --label: #e6e6e6;
    --field-top: #fafafa;
    --field-bottom: #dcdcdc;
    --field-text: #333333;
    --icon-green: #a9cf5b;
    --white: #ffffff;
  }
  * { box-sizing: border-box; margin: 0; padding: 0; }
  html, body {
    width: 676px; height: 1200px; overflow: hidden;
    background: var(--page-bg);
    font-family: "Noto Sans", Verdana, sans-serif;
  }
  .screen { position: relative; width: 676px; height: 1200px; }

  .brand {
    position: absolute; left: 0; right: 0; top: 56px;
    text-align: center;
  }
  .brand-name {
    font-size: 32px; font-weight: 400; color: var(--brand-text);
  }

  .login-frame {
    position: absolute; left: 62px; top: 251px;
    width: 550px; height: 275px;
    background: var(--frame); border-radius: 22px;
    padding: 11px 10px 11px 11px;
  }
  .login-card {
    display: flex; width: 100%; height: 100%;
    border-radius: 14px; overflow: hidden;
  }
  .login-form {
    position: relative; width: 429px; height: 100%;
    background: radial-gradient(ellipse at 45% 30%, var(--panel-dark-hi), var(--panel-dark) 75%);
    color: var(--label);
  }
  .login-title {
    position: absolute; left: 18px; top: 10px;
    font-size: 27px; font-weight: 400; color: var(--white); letter-spacing: 0.5px;
  }
  .login-divider {
    position: absolute; left: 0; right: 0; top: 54px;
    border-top: 1px solid #1f1f1f; border-bottom: 1px solid #444;
  }
  .field-label { position: absolute; top: 97px; font-size: 16px; }
  .field-label.username { left: 22px; }
  .field-label.password { left: 223px; }

  .field {
    position: absolute; top: 139px; width: 171px; height: 34px;
    border-radius: 5px;
    background: linear-gradient(var(--field-top), var(--field-bottom));
    border: 1px solid #bbb;
    display: flex; align-items: center; justify-content: space-between;
    padding: 0 10px 0 18px;
    color: var(--field-text); font-size: 16px;
  }
  .field.username { left: 21px; }
  .field.password { left: 224px; padding-left: 10px; }
  .dots { display: flex; gap: 3px; }
  .dots span { width: 12px; height: 12px; border-radius: 50%; background: #333; }

  .remember {
    position: absolute; left: 19px; top: 193px;
    display: flex; align-items: center; gap: 10px; font-size: 14px;
  }
  .radio {
    width: 24px; height: 24px; border-radius: 50%;
    background: linear-gradient(#f4f4f4, #cfcfcf);
    display: flex; align-items: center; justify-content: center;
  }
  .radio::after {
    content: ""; width: 11px; height: 11px; border-radius: 50%; background: #2d2d2d;
  }
  .forgot {
    position: absolute; left: 209px; top: 196px; font-size: 14px; white-space: nowrap;
  }
  .forgot em { font-style: italic; }

  .login-go {
    position: relative; flex: 1; height: 100%;
    background: linear-gradient(var(--accent), var(--accent-deep));
    color: var(--white);
  }
  .go-chevron { position: absolute; left: 24px; top: 42px; }
  .go-label {
    position: absolute; left: 0; right: 0; top: 185px;
    text-align: center; font-size: 27px;
  }

  .signup-frame {
    position: absolute; left: 67px; top: 964px;
    width: 538px; height: 106px;
    background: var(--frame); border-radius: 12px; padding: 5px;
  }
  .signup-button {
    width: 100%; height: 100%; border-radius: 8px;
    background: linear-gradient(var(--accent), var(--accent-deep));
    color: var(--white); font-size: 27px; letter-spacing: 0.5px;
    display: flex; align-items: center; justify-content: center;
  }
</style>
</head>
<body>
<main class="screen">
  <header class="brand">
    <span class="brand-name">Brindlewood Networks</span>
  </header>

  <section class="login-frame">
    <div class="login-card">
      <div class="login-form">
        <h1 class="login-title">LOGIN</h1>
        <div class="login-divider"></div>
        <span class="field-label username">Username:</span>
        <span class="field-label password">Password:</span>
        <div class="field username">
          <span>admin</span>
          <svg width="20" height="20" viewBox="0 0 20 20" aria-hidden="true">
            <circle cx="10" cy="6" r="5" fill="var(--icon-green)"/>
            <path d="M1 20 C1 12 19 12 19 20 Z" fill="var(--icon-green)"/>
          </svg>
        </div>
        <div class="field password">
          <span class="dots"><span></span><span></span><span></span><span></span></span>
          <svg width="20" height="20" viewBox="0 0 20 20" aria-hidden="true">
            <path d="M5 9 V6 a5 5 0 0 1 10 0 V9" fill="none" stroke="var(--icon-green)" stroke-width="2"/>
            <rect x="1" y="8" width="18" height="12" rx="1" fill="var(--icon-green)"/>
          </svg>
        </div>
        <label class="remember"><span class="radio"></span>Remember me</label>
        <span class="forgot">Forgot <em>username</em> or <em>password</em>?</span>
      </div>
      <div class="login-go">
        <svg class="go-chevron" width="50" height="74" viewBox="0 0 50 74" aria-hidden="true">
          <path d="M10 8 L38 37 L10 66" fill="none" stroke="#e8e8e8" stroke-width="16" stroke-linecap="round" stroke-linejoin="round"/>
        </svg>
        <span class="go-label">GO</span>
      </div>
    </div>
  </section>

  <div class="signup-frame">
    <div class="signup-button">SIGN UP</div>
  </div>
</main>
</body>
</html>
```